Harbourview Motor Works Business Card Design

Looking for a "clean and sharp" looking business card. Really like the design in the attachment? Our colours are black, white and red. Would like to see the curves with some metallic/shimmer colour and wouldn't mind if the front background was high gloss black.

Target Market(s)

Car owners

Industry/Entity Type

Business

Contact Information for Business Card

On the front:
Harbourview Motor Works
ABN 731 902 514 67
48 Brenton Parade
Tewantin Q 4539
Phone: 07 5418 9276
On the back:
General Servicing
Timing Belts
Brake Repairs
Injector Servicing
Suspension
Log Book Servicing
Clutches
Email: harbourviewmotorworks@mailbox-example.com
All work guaranteed by Qualified Master Mechanic 20 years experience

Colors
ffffff
ec1f27
000000

Requirements
Must have
• Must have the curved lines above the text in some type of metallic

```html
<!DOCTYPE html>
<html lang="en">
<head>
<meta charset="utf-8">
<title>Harbourview Motor Works – Business Card</title>
<link rel="stylesheet" href="https://fonts.googleapis.com/css2?family=Exo+2:ital,wght@0,400;0,600;0,700;1,400&display=swap">
<style>
  :root {
    --stage: #585858;
    --card-black: #050608;
    --white: #ffffff;
    --silver-light: #f4f4f4;
    --silver-mid: #8e8e8e;
    --silver-dark: #d4d4d4;
    --silver-deep: #5c5c5c;
    --red: #ec1f27;
    --rule: #c8c8c8;
  }
  html, body {
    margin: 0;
    padding: 0;
    width: 1200px;
    height: 900px;
    overflow: hidden;
    background: var(--stage);
  }
  .canvas {
    position: relative;
    width: 1200px;
    height: 900px;
  }
  .card {
    position: absolute;
    top: 293px;
    width: 519px;
    height: 315px;
    background: var(--card-black);
  }
  .card--front {
    left: 67px;
    background: linear-gradient(160deg, #16181c 0%, var(--card-black) 45%, #000000 100%);
  }
  .card--back { left: 614px; }
  .card svg { display: block; }
  .card text {
    font-family: "Exo 2", sans-serif;
    fill: var(--white);
  }
  .abn { font-size: 15px; font-style: italic; }
  .business-name { font-size: 32px; font-weight: 700; }
  .address { font-size: 19px; letter-spacing: 1.6px; }
  .phone { font-size: 20px; letter-spacing: 0.5px; }
  .services { font-size: 19px; }
  .email { font-size: 16px; }
  .guarantee { font-size: 14px; font-style: italic; }
  .guarantee .experience { fill: var(--red); font-weight: 700; font-style: normal; }
  .thin-rule { stroke: var(--white); stroke-width: 0.8; }
  .silver-rule { stroke: var(--rule); stroke-width: 2; }
  .metal-curve { fill: none; stroke: url(#metal-sweep); stroke-linecap: round; }
  .metal-curve--main { stroke-width: 2.2; }
  .metal-curve--fine { stroke-width: 1; opacity: 0.7; }
</style>
</head>
<body>
<main class="canvas">
  <section class="card card--front" aria-label="Card front">
    <svg width="519" height="315" viewBox="0 0 519 315">
      <defs>
        <linearGradient id="metallic" x1="0" y1="0" x2="0" y2="1">
          <stop offset="0" stop-color="var(--silver-light)"/>
          <stop offset="0.5" stop-color="var(--silver-dark)"/>
          <stop offset="1" stop-color="var(--silver-mid)"/>
        </linearGradient>
        <linearGradient id="metal-sweep" x1="0" y1="0" x2="1" y2="0">
          <stop offset="0" stop-color="var(--silver-deep)" stop-opacity="0"/>
          <stop offset="0.25" stop-color="var(--silver-mid)"/>
          <stop offset="0.55" stop-color="var(--silver-light)"/>
          <stop offset="0.8" stop-color="var(--silver-dark)"/>
          <stop offset="1" stop-color="var(--silver-deep)" stop-opacity="0"/>
        </linearGradient>
      </defs>
      <g class="metal-curves">
        <path class="metal-curve metal-curve--main" d="M20 108 C 140 40, 330 30, 500 86"/>
        <path class="metal-curve metal-curve--fine" d="M40 100 C 160 48, 340 46, 505 96"/>
        <path class="metal-curve metal-curve--fine" d="M10 96 C 120 30, 320 18, 495 70"/>
      </g>
      <line class="thin-rule" x1="32" y1="120" x2="324" y2="120"/>
      <text class="abn" x="488" y="122" text-anchor="end">ABN 731 902 514 67</text>
      <text class="business-name" x="259" y="156" text-anchor="middle" textLength="458" lengthAdjust="spacingAndGlyphs" style="fill:url(#metallic)">HARBOURVIEW MOTOR WORKS</text>
      <text class="address" x="259" y="179" text-anchor="middle">48 Brenton Parade Tewantin Q 4539</text>
      <line class="thin-rule" x1="52" y1="188" x2="179" y2="188"/>
      <line class="thin-rule" x1="339" y1="188" x2="466" y2="188"/>
      <text class="phone" x="259" y="205" text-anchor="middle">07 5418 9276</text>
    </svg>
  </section>

  <section class="card card--back" aria-label="Card back">
    <svg width="519" height="315" viewBox="0 0 519 315">
      <text class="services" x="260" y="135" text-anchor="middle">General Servicing Timing Belts Brake Repairs Injector</text>
      <text class="services" x="260" y="158" text-anchor="middle">Servicing Suspension Log Book Servicing Clutches</text>
      <text class="email" x="260" y="191" text-anchor="middle">harbourviewmotorworks@mailbox-example.com</text>
      <line class="silver-rule" x1="0" y1="258" x2="519" y2="258"/>
      <text class="guarantee" x="260" y="278" text-anchor="middle">All work guaranteed by Qualified Master Mechanic <tspan class="experience">20 years experience</tspan></text>
    </svg>
  </section>
</main>
</body>
</html>
```